The Lantern Protocol: A Practical Guide for Tending Old Orchards

This will be for both the hard cover and paperback version. A core theme of the book and what we want to cover to convey is the journey or transformation to "happiness". Concepts such as road/pathway, mountain top, sunrise, dark to bright colors, out-of-focus to in-focus, clouds parting, etc., all represent this idea. I am attaching a 1-page book summary for more information. I like the idea of the subtitle being in a gold seal, but that is not necessary. I am open to any designs, but it should at least be conceptually related to the book.

```html
<!DOCTYPE html>
<html lang="en">
<head>
<meta charset="utf-8">
<title>The Lantern Protocol — Cover</title>
<link rel="stylesheet" href="https://fonts.googleapis.com/css2?family=Cinzel:wght@400;500&family=Great+Vibes&family=Oswald:wght@300&display=swap">
<style>
  :root {
    --page-bg: #e9e9e9;
    --paper: #f6f5f1;
    --mist: #dfe3e1;
    --water: #c9d2d1;
    --teal-deep: #3d5656;
    --band: #253b3c;
    --cliff: #8a6230;
    --cliff-dark: #4a3620;
    --ink: #2a2a2a;
    --title: #ffffff;
  }
  * { margin: 0; padding: 0; box-sizing: border-box; }
  html, body {
    width: 1200px;
    height: 920px;
    overflow: hidden;
    background: var(--page-bg);
  }
  .stage {
    width: 1200px;
    height: 920px;
    display: flex;
    align-items: center;
    justify-content: center;
  }
  .cover {
    position: relative;
    width: 550px;
    height: 860px;
    background: var(--paper);
    overflow: hidden;
  }
  .cover-art {
    position: absolute;
    left: 0;
    top: 150px;
    width: 550px;
    height: 630px;
    display: block;
  }
  .subtitle {
    position: absolute;
    top: 54px;
    left: 0;
    right: 0;
    text-align: center;
    font-family: "Oswald", sans-serif;
    font-weight: 300;
    font-size: 23px;
    letter-spacing: 0.2px;
    color: var(--ink);
  }
  .title-block {
    position: absolute;
    top: 405px;
    left: 0;
    right: 0;
    text-align: center;
    color: var(--title);
  }
  .title-lead {
    display: block;
    font-family: "Great Vibes", cursive;
    font-size: 70px;
    line-height: 0.9;
    margin-left: -10px;
  }
  .title-main {
    display: block;
    font-family: "Cinzel", serif;
    font-weight: 400;
    font-size: 66px;
    line-height: 1.08;
    letter-spacing: 0.5px;
  }
  .author-band {
    position: absolute;
    left: 0;
    bottom: 0;
    width: 100%;
    height: 84px;
    background: var(--band);
    display: flex;
    align-items: center;
    justify-content: center;
  }
  .author {
    font-family: "Cinzel", serif;
    font-weight: 400;
    font-size: 40px;
    letter-spacing: 1px;
    color: var(--title);
  }
</style>
</head>
<body>
  <main class="stage">
    <article class="cover">
      <svg class="cover-art" viewBox="0 0 550 630" role="img" aria-label="Photograph of a tall misty waterfall between brown cliffs with a small figure standing at its base">
        <defs>
          <linearGradient id="sky-fade" x1="0" y1="0" x2="0" y2="1">
            <stop offset="0" stop-color="#f6f5f1"/>
            <stop offset="0.12" stop-color="#e6e8e4"/>
            <stop offset="0.5" stop-color="#b9c6c5"/>
            <stop offset="0.85" stop-color="#7f9493"/>
            <stop offset="1" stop-color="#3d5656"/>
          </linearGradient>
          <linearGradient id="cliff-left" x1="0" y1="0" x2="1" y2="0">
            <stop offset="0" stop-color="#5a4123"/>
            <stop offset="0.6" stop-color="#8a6230"/>
            <stop offset="1" stop-color="#a3865a" stop-opacity="0"/>
          </linearGradient>
          <linearGradient id="cliff-right" x1="1" y1="0" x2="0" y2="0">
            <stop offset="0" stop-color="#4a3620"/>
            <stop offset="0.7" stop-color="#6e4f2c"/>
            <stop offset="1" stop-color="#6e4f2c" stop-opacity="0"/>
          </linearGradient>
        </defs>
        <rect width="550" height="630" fill="url(#sky-fade)"/>
        <rect x="0" y="50" width="150" height="580" fill="url(#cliff-left)"/>
        <rect x="420" y="260" width="130" height="370" fill="url(#cliff-right)"/>
      </svg>

      <p class="subtitle">A Practical Guide for Tending Old Orchards</p>

      <h1 class="title-block">
        <span class="title-lead">The</span>
        <span class="title-main">Lantern</span>
        <span class="title-main">Protocol</span>
      </h1>

      <footer class="author-band">
        <p class="author">Martin L. Hale</p>
      </footer>
    </article>
  </main>
</body>
</html>
```